Corvale Masonry

i need a brochure (more of a company profile for a company that has been in business for a long time). Unfortunately we have never had a proper company profile so basically im looking for a professional brochure that shows the strength of the company and what it does.
CORVALE MASONRY is a general contracting & construction company based in Jeddah with operations all over the region. We focus on civil/structural works and have the capabilities of executing electro-mechanical, finishing works and turnkey projects.

Reason: I stil need more designs from other invited designers that have accepted my invitation.

To all designers

I have extended the deadline until December 28th...i hope this will help you with your work

happy holidays to everyone!

Target Market(s)

government, real estate developers, private client/investors

Industry/Entity Type

Construction

Requirements
Must have
• -file named prequalifictaion has all the information necessary to fill up the brochure.
-22-30 pages
-using only the best photos that i have uploaded named project pics.
-A bi-fold brochure measuring 8inches high by 10 inches wide, however i am open for suggestions.
-sorry everyone, i dont have my logo in eps format
Should not have
• too many colors

```html
<!DOCTYPE html>
<html lang="en">
<head>
<meta charset="utf-8">
<title>Corvale Masonry – Personnel &amp; Manpower</title>
<link rel="stylesheet" href="https://fonts.googleapis.com/css2?family=Saira:wght@400;600;700&family=Ubuntu:wght@300;400;500;700&display=swap">
<style>
:root{
  --navy:#1c3f6e;
  --grey:#808285;
  --grey-text:#8a8c8e;
  --row-a:#e6e7e8;
  --row-b:#d1d3d4;
  --ink:#231f20;
  --paper:#ffffff;
  --frame:#b3b5b7;
}
*{box-sizing:border-box;margin:0;padding:0}
html,body{width:1200px;height:900px;overflow:hidden;background:var(--paper)}
body{position:relative;font-family:"Ubuntu",sans-serif;color:var(--ink)}
.spread{position:absolute;left:40px;top:0;width:1123px;height:900px;border-left:1px solid #d8d8d8;border-right:1px solid #d8d8d8}
.fold{position:absolute;left:601px;top:0;width:1px;height:845px;background:#dcdcdc}
.top-band{position:absolute;top:0;height:108px;width:561px;background:linear-gradient(180deg,#c9cacc 0%,#b9bbbd 70%,#e9e9ea 100%)}
.top-band.left{left:41px}.top-band.right{left:602px}
.footer{position:absolute;left:40px;top:845px;width:1123px;height:55px;background:var(--grey);display:flex;color:#fff;font-family:"Saira",sans-serif;font-weight:600}
.footer div{flex:1;text-align:center;padding-top:9px;font-size:15px;line-height:16px;letter-spacing:1px}
.footer b{display:block;font-size:11.5px;font-weight:600;letter-spacing:.3px}
.tab{position:absolute;top:700px;width:16px;height:90px;background:var(--navy)}
.tab.left{left:40px;border-radius:0 6px 6px 0}.tab.right{left:1147px;border-radius:6px 0 0 6px}
.page-title{position:absolute;left:155px;top:126px;width:331px;height:36px;border-top:2px solid var(--grey);border-bottom:2px solid var(--grey);text-align:center;white-space:nowrap;font-family:"Saira",sans-serif;font-weight:700;font-size:21px;letter-spacing:1.2px;line-height:33px;color:var(--navy)}
.running-head{position:absolute;left:700px;top:131px;width:366px;text-align:center;white-space:nowrap;font-family:"Saira",sans-serif;font-weight:600;font-size:15px;letter-spacing:.8px;color:var(--grey-text)}
.intro{position:absolute;left:97px;top:212px;font-size:12px}
.staff{position:absolute;left:97px;top:239px;width:447px;border-collapse:collapse;font-size:12.5px;font-weight:300}
.staff th{background:var(--navy);color:#fff;font-weight:400;font-size:10.5px;text-align:left;vertical-align:top;padding:2px 6px;height:30px;line-height:12.5px;border-left:2px solid #fff}
.staff th:first-child{border-left:none}
.staff td{padding:0 6px;height:18.2px;line-height:18px;white-space:nowrap}
.staff tbody tr:nth-child(odd){background:var(--row-a)}
.staff tbody tr:nth-child(even){background:var(--row-b)}
.staff tbody tr:first-child td{border-top:5px solid #fff}
.staff tbody tr:last-child{border-bottom:1.5px solid var(--navy)}
.c1{width:163px}.c2{width:197px}
.photo-frame{position:absolute;left:97px;top:636px;width:504px;height:175px;background:var(--frame)}
.photo{position:absolute;left:5px;top:5px;width:442px;height:165px;background:linear-gradient(160deg,#c9c2b1 0%,#8e7f69 45%,#5c5146 100%)}
.section-label{position:absolute;left:659px;font-size:12.5px;font-weight:700}
.note{position:absolute;left:659px;top:448px;font-size:11.5px}
.rule{position:absolute;left:659px;width:448px;border-top:2px dotted #555}
.role{position:absolute;text-align:center}
.role .figure{margin:0 auto;background:#1a1a1a;opacity:.85;border-radius:3px}
.role .label{position:absolute;left:0;right:0;font-family:"Saira",sans-serif;font-weight:600;font-size:11.5px;letter-spacing:.3px;color:var(--ink);border-bottom:1px dotted #999;padding-bottom:1px;white-space:nowrap}
.role .sub{position:absolute;left:-20px;right:-20px;font-size:10px;color:#333;white-space:nowrap}
.bubble{position:absolute;width:60px;height:60px}
.bubble span{position:absolute;left:0;top:0;width:52px;height:52px;line-height:52px;text-align:center;font-family:"Saira",sans-serif;font-weight:600;font-size:20px;letter-spacing:.5px;color:#fff}
</style>
</head>
<body>
<div class="spread"></div>
<div class="fold"></div>
<div class="top-band left" role="img" aria-label="Dotted pattern band with a city skyline cut-out"></div>
<div class="top-band right" role="img" aria-label="Dotted pattern band with a city skyline cut-out"></div>

<h1 class="page-title">PERSONNEL &amp; MANPOWER</h1>
<p class="intro">Our Technical staff varies between Lebanese and Syrian Engineers and Foremen.</p>

<table class="staff">
  <thead><tr><th class="c1">Name</th><th class="c2">Present Position in<br>Organization</th><th>Years of<br>Construct. Exp.</th></tr></thead>
  <tbody>
    <tr><td>Karim Haddad</td><td>Managing Director</td><td>40</td></tr>
    <tr><td>Nabil R. Farouq</td><td>General Manager</td><td>25</td></tr>
    <tr><td>Samir Al-Qadi</td><td>Finance Controller</td><td>12</td></tr>
    <tr><td>Rashid M. Qureshi</td><td>Technical Office Manager</td><td>13</td></tr>
    <tr><td>Tahir Nawaz</td><td>Technical Office Engineer</td><td>12</td></tr>
    <tr><td>Walid S. Marouf</td><td>Project Manager</td><td>19</td></tr>
    <tr><td>Mohd. Imran Latif</td><td>Project Manager</td><td>18</td></tr>
    <tr><td>10 Nos.</td><td>Site Engineers</td><td>05</td></tr>
    <tr><td>Fadi Karam</td><td>Chief Surveyor</td><td>12</td></tr>
    <tr><td>4 Nos.</td><td>Assis. Surveyor</td><td>06</td></tr>
    <tr><td>Abdul Wahid Saleem</td><td>AutoCAD</td><td>07</td></tr>
    <tr><td>Yousef Nader</td><td>General Foreman</td><td>16</td></tr>
    <tr><td>Ramzi Khalil</td><td>General Foreman</td><td>16</td></tr>
    <tr><td>Hamdi Adel Hamdi</td><td>Foreman</td><td>14</td></tr>
    <tr><td>Abdul Majeed Omar</td><td>Foreman</td><td>14</td></tr>
    <tr><td>Mohd. Akram Bashir</td><td>Assistant Foreman</td><td>16</td></tr>
    <tr><td>Mohd. Javed Noor</td><td>Assistant Foreman</td><td>10</td></tr>
    <tr><td>5 Nos. (Saudis)</td><td>Followers</td><td>02</td></tr>
    <tr><td>Ziad Mansour</td><td>Personnel Assistant</td><td>10</td></tr>
  </tbody>
</table>

<div class="photo-frame"><div class="photo" role="img" aria-label="Photo of workers welding steel in a covered site workshop"></div></div>

<h2 class="running-head">PERSONNEL &amp; MANPOWER</h2>

<p class="section-label" style="top:213px">Site Overhead:</p>

<svg width="0" height="0" style="position:absolute">
  <defs>
    <symbol id="bubble" viewBox="0 0 60 60">
      <circle cx="26" cy="26" r="26" fill="#1c3f6e"/>
      <path d="M6 40 L2 58 L20 48 Z" fill="#1c3f6e"/>
    </symbol>
  </defs>
</svg>

<div class="bubble" style="left:729px;top:247px"><svg width="60" height="60"><use href="#bubble"/></svg><span>04</span></div>
<div class="bubble" style="left:824px;top:247px"><svg width="60" height="60"><use href="#bubble"/></svg><span>04</span></div>
<div class="bubble" style="left:958px;top:247px"><svg width="60" height="60"><use href="#bubble"/></svg><span>04</span></div>
<div class="bubble" style="left:1064px;top:247px"><svg width="60" height="60"><use href="#bubble"/></svg><span>04</span></div>

<div class="role" style="left:659px;top:288px;width:80px"><div class="figure" role="img" aria-label="Silhouette of a driver beside a truck" style="width:76px;height:74px"></div><p class="label" style="top:79px">DRIVERS</p></div>
<div class="role" style="left:763px;top:300px;width:90px"><div class="figure" role="img" aria-label="Silhouette of a time keeper holding a clipboard" style="width:26px;height:62px"></div><p class="label" style="top:67px">TIME KEEPERS</p></div>
<div class="role" style="left:889px;top:296px;width:110px"><div class="figure" role="img" aria-label="Silhouette of a store keeper carrying boxes" style="width:34px;height:66px"></div><p class="label" style="top:71px">STORE KEEPERS</p></div>
<div class="role" style="left:1039px;top:300px;width:68px"><div class="figure" role="img" aria-label="Silhouette of a guard" style="width:26px;height:62px"></div><p class="label" style="top:67px">GUARDS</p></div>

<div class="rule" style="top:407px"></div>

<p class="section-label" style="top:427px">Man Power:</p>
<p class="note">Consists of (90% Pakistani &amp; remaining Egyptian) + 23 Saudis</p>

<div class="bubble" style="left:709px;top:488px"><svg width="60" height="60"><use href="#bubble"/></svg><span>150</span></div>
<div class="bubble" style="left:832px;top:488px"><svg width="60" height="60"><use href="#bubble"/></svg><span>175</span></div>
<div class="bubble" style="left:948px;top:488px"><svg width="60" height="60"><use href="#bubble"/></svg><span>25</span></div>
<div class="bubble" style="left:1056px;top:488px"><svg width="60" height="60"><use href="#bubble"/></svg><span>50</span></div>

<div class="role" style="left:659px;top:540px;width:92px"><div class="figure" role="img" aria-label="Silhouette of a carpenter carrying a plank" style="width:48px;height:62px"></div><p class="label" style="top:67px">CARPENTERS</p></div>
<div class="role" style="left:773px;top:532px;width:94px"><div class="figure" role="img" aria-label="Silhouette of a steel fixer" style="width:24px;height:70px"></div><p class="label" style="top:75px">STEEL FIXERS</p></div>
<div class="role" style="left:890px;top:536px;width:90px"><div class="figure" role="img" aria-label="Silhouette of a mason" style="width:26px;height:66px"></div><p class="label" style="top:71px">MASONS</p></div>
<div class="role" style="left:995px;top:544px;width:112px"><div class="figure" role="img" aria-label="Silhouette of a labourer with a shovel" style="width:40px;height:58px"></div><p class="label" style="top:63px">NORMAL LABOR</p></div>

<div class="bubble" style="left:733px;top:661px"><svg width="60" height="60"><use href="#bubble"/></svg><span>10</span></div>
<div class="bubble" style="left:908px;top:661px"><svg width="60" height="60"><use href="#bubble"/></svg><span>03</span></div>

<div class="role" style="left:669px;top:712px;width:96px"><div class="figure" role="img" aria-label="Silhouette of a kneeling tile fixer" style="width:40px;height:32px"></div><p class="label" style="top:37px">MULTI TRADES</p><p class="sub" style="top:55px">(Tile Fixers, Gypsum, ...etc.)</p></div>
<div class="role" style="left:813px;top:682px;width:147px"><div class="figure" role="img" aria-label="Silhouette of an electrician on a ladder" style="width:42px;height:62px"></div><p class="label" style="top:67px">ELECTRO MECHANICAL</p></div>

<div class="rule" style="top:798px"></div>

<div class="tab left"></div>
<div class="tab right"></div>

<footer class="footer">
  <div><b>Corvale Masonry</b>. 4 .</div>
  <div><b>Corvale Masonry</b>. 5 .</div>
</footer>
</body>
</html>
```